New Law Firm needs a business card design

I need a business card for my new law firm called Tansey Wills and Probate. I would like designs to use my logo attached. My firm is new and modern. I like the colors orange, white, grey and black. The design I will chose will be one which uses color well, one which looks impressive, smart and modern.

Target Market(s)

Adults aged 30 to 50 seeking professional advice.

Industry/Entity Type

Law Firm

Requirements
Must have
• My logo which is attached.

Must have a modern font, similar to my logo and draft business card.
Should not have
• Any symbols about law, such as scales etc.

```html
<!DOCTYPE html>
<html lang="en">
<head>
<meta charset="utf-8">
<title>Tansey Wills &amp; Probate – Business Card</title>
<link rel="stylesheet" href="https://fonts.googleapis.com/css2?family=Questrial&display=swap">
<style>
  :root {
    --page: #ffffff;
    --card: #ffffff;
    --ink: #2b2b2b;
    --grey: #6d6d6d;
    --orange: #f39a3c;
    --icon: #111111;
  }
  * { margin: 0; padding: 0; box-sizing: border-box; }
  html, body {
    width: 1200px;
    height: 1000px;
    overflow: hidden;
    background: var(--page);
    font-family: "Questrial", "Helvetica Neue", Arial, sans-serif;
  }
  .canvas { position: relative; width: 1200px; height: 1000px; }

  .card {
    position: absolute;
    left: 282px;
    width: 658px;
    height: 384px;
    background: var(--card);
    box-shadow: 0 1px 4px rgba(0,0,0,0.4);
    overflow: hidden;
  }
  .card--front { top: 82px; }
  .card--back { top: 514px; }

  .card__rule {
    position: absolute;
    left: 0;
    top: 349px;
    width: 100%;
    height: 2px;
    background: var(--orange);
  }

  /* Firm name set as plain text */
  .brand {
    position: absolute;
    color: var(--grey);
    text-transform: uppercase;
    line-height: 1.15;
  }
  .brand--large {
    right: 76px;
    top: 78px;
    font-size: 19.5px;
    letter-spacing: 1.5px;
    text-align: right;
  }
  .brand--small {
    left: 31px;
    top: 282px;
    font-size: 12px;
    letter-spacing: 1.2px;
    text-align: left;
  }

  /* Front: name block */
  .person {
    position: absolute;
    left: 38px;
    top: 266px;
  }
  .person__name {
    font-size: 31px;
    color: var(--ink);
    line-height: 1.1;
  }
  .person__role {
    font-size: 21px;
    color: var(--grey);
    margin-left: 8px;
  }
  .person__credentials {
    font-size: 21px;
    color: var(--orange);
    margin-top: 3px;
  }

  /* Back: contact list */
  .contacts {
    position: absolute;
    right: 63px;
    top: 84px;
    list-style: none;
  }
  .contacts__item {
    display: flex;
    justify-content: flex-end;
    align-items: center;
    height: 31px;
    font-size: 21.5px;
    color: var(--grey);
  }
  .contacts__icon {
    width: 27px;
    height: 26px;
    margin-left: 20px;
    flex: none;
  }
</style>
</head>
<body>
<main class="canvas">

  <section class="card card--front" aria-label="Business card front">
    <p class="brand brand--large">Tansey<br>Wills &amp; Probate</p>

    <div class="person">
      <p class="person__name">Daniel Marsh<span class="person__role">Lawyer</span></p>
      <p class="person__credentials">Assoc.Deg.Law, BLJSt, LLB, Grad Dip Law.</p>
    </div>

    <div class="card__rule"></div>
  </section>

  <section class="card card--back" aria-label="Business card back">
    <ul class="contacts">
      <li class="contacts__item">Address: To be confirmed
        <svg class="contacts__icon" viewBox="0 0 30 28" aria-hidden="true">
          <rect x="3" y="6" width="24" height="16" fill="none" stroke="var(--icon)" stroke-width="1.6"/>
          <path d="M3 6 L15 16 L27 6 M3 22 L12 13.5 M27 22 L18 13.5" fill="none" stroke="var(--icon)" stroke-width="1.6"/>
        </svg>
      </li>
      <li class="contacts__item">Phone: To be confirmed
        <svg class="contacts__icon" viewBox="0 0 30 28" aria-hidden="true">
          <rect x="10" y="3" width="11" height="21" rx="1.5" fill="var(--icon)"/>
          <rect x="11.5" y="5" width="8" height="15" fill="#fff"/>
          <circle cx="15.5" cy="22" r="1" fill="#fff"/>
        </svg>
      </li>
      <li class="contacts__item">Fax: To be confirmed
        <svg class="contacts__icon" viewBox="0 0 30 28" aria-hidden="true">
          <rect x="8" y="1" width="14" height="13" fill="#fff" stroke="var(--icon)" stroke-width="1.3"/>
          <path d="M10.5 4.5h9M10.5 7.5h9M10.5 10.5h9" stroke="var(--icon)" stroke-width="1"/>
          <rect x="2" y="14" width="26" height="13" fill="#fff" stroke="var(--icon)" stroke-width="1.4"/>
          <path d="M8 22c0-5 14-5 14 0h-3.5v-1.5c-2-1.5-5-1.5-7 0V22z" fill="var(--icon)"/>
        </svg>
      </li>
      <li class="contacts__item">Email: daniel@tanseyprobate.com.au
        <svg class="contacts__icon" viewBox="0 0 30 28" aria-hidden="true">
          <rect x="3" y="6" width="24" height="16" fill="none" stroke="var(--icon)" stroke-width="1.6"/>
          <path d="M3 6 L11 13 M27 6 L19 13 M3 22 L11 15 M27 22 L19 15" fill="none" stroke="var(--icon)" stroke-width="1.6"/>
          <circle cx="15" cy="14" r="3.2" fill="none" stroke="var(--icon)" stroke-width="1.3"/>
          <circle cx="15" cy="14" r="1.2" fill="var(--icon)"/>
        </svg>
      </li>
    </ul>

    <p class="brand brand--small">Tansey<br>Wills &amp; Probate</p>

    <div class="card__rule"></div>
  </section>

</main>
</body>
</html>
```